New Service Brochure for The Larkmere Spa

Hi All! We are looking for a new brochure design- tri-fold, double sided, and full color. We are a certified Clear Spa for men and women in the heart of the Catskill Mountains of upstate New York. Our clients would describe us as laid back luxury with no pretensions and a home away from home vibe. Our font is Avalon. Key colors are black, white and gold. Looking for an inviting, clean, and modern/minimalist spread with a touch of elegance. No orchid imagery, please. I would like our "Clear Spa" logo on cover, too please. Front cover image with with logo and "Clear Spa" Sticker . Bottom of back with contact info. We would prefer massages go on left inside page, facials in middle and right inside, nails on back left, but we are open to new or different layout proposals. Thank you!

Target Market(s)

Men & Women.

Industry/Entity Type

Health And Wellness

Font styles to use
Other font styles liked:
• Avalon is our signature font

Requirements
Must have
• Easy on the eyes.
Nice to have
• Negative space.
Should not have
• No orchids. Busy lines and wild colors.

```html
<!DOCTYPE html>
<html lang="en">
<head>
<meta charset="utf-8">
<title>The Larkmere Spa – Service Brochure</title>
<link href="https://fonts.googleapis.com/css2?family=Cormorant+Garamond:wght@500&family=Montserrat:wght@400;600;700&family=Open+Sans:wght@400;700&display=swap" rel="stylesheet">
<style>
:root{
  --gold:#c9a227;
  --ink:#231f20;
  --charcoal:#2b2829;
  --grey:#4a4748;
  --paper:#ffffff;
  --text:#3a3738;
  --backdrop:#e9e6e1;
}
*{box-sizing:border-box;margin:0;padding:0}
html,body{width:1200px;height:1200px;overflow:hidden;background:var(--backdrop)}
body{position:relative;font-family:"Open Sans",sans-serif;color:var(--text)}
.sheet{position:absolute;left:222px;width:756px;height:586px;display:grid;grid-template-columns:repeat(3,1fr);background:var(--paper);box-shadow:0 4px 14px rgba(0,0,0,.25)}
.sheet--outside{top:8px}
.sheet--inside{top:606px}
.panel{position:relative;overflow:hidden;border-right:1px solid #e4e4e4}
.panel:last-child{border-right:0}
.panel--list{padding:18px 21px 16px;display:flex;flex-direction:column}
.section-title{display:flex;align-items:flex-end;border-bottom:1.5px solid var(--grey);margin-bottom:6px}
.section-title span{background:var(--grey);color:#fff;font-family:"Montserrat",sans-serif;font-weight:700;font-size:12px;letter-spacing:.5px;padding:1px 16px 0 4px;clip-path:polygon(0 0,calc(100% - 10px) 0,100% 100%,0 100%)}
.section-title i{margin-left:auto;width:11px;height:11px;border:2px solid var(--gold);border-radius:50%;margin-bottom:2px}
.lead{font-size:6.5px;line-height:1.4;text-align:justify}
.items{flex:1;display:flex;flex-direction:column;justify-content:space-between;margin-top:10px}
.item-head{display:flex;align-items:flex-end;border-bottom:.8px solid #777;margin-bottom:3px}
.item-name{font-family:"Montserrat",sans-serif;font-weight:600;font-size:7.6px;color:var(--ink);padding-bottom:1px}
.price{margin-left:auto;background:var(--gold);color:#fff;font-family:"Montserrat",sans-serif;font-weight:700;font-size:7.4px;padding:1px 5px 0 10px;clip-path:polygon(7px 0,100% 0,100% 100%,0 100%)}
.item p{font-size:6.4px;line-height:1.42;text-align:justify}
.item b{font-weight:700}
.wordmark{font-family:"Cormorant Garamond",serif;font-weight:500;text-align:center;letter-spacing:1px;line-height:.9}
.wordmark .w-the{display:block;font-size:.6em}
.wordmark .w-name{display:block;font-size:1em}
.wordmark .w-spa{display:block;font-size:.8em}
.tagline{font-family:"Montserrat",sans-serif;font-size:7px;text-align:center}
.photo{background:radial-gradient(circle at 40% 40%,#e8cdb4,#a97a57 60%,#5c4536)}
/* outside middle */
.panel--dark{background:var(--charcoal);color:#fff}
.panel--dark .photo-band{position:absolute;left:0;top:0;width:100%;height:300px;background:linear-gradient(180deg,#8d8a89 0%,#5b5758 55%,var(--charcoal) 100%)}
.panel--dark .wordmark{position:absolute;top:312px;width:100%;font-size:30px;color:#fff}
.panel--dark .tagline{position:absolute;top:404px;width:100%;color:#ddd}
.partner{position:absolute;left:22px;top:456px;width:48px;text-align:center}
.partner .seal{width:44px;height:58px;border:2px solid var(--gold);background:linear-gradient(135deg,#a8832a,#e4c977,#a8832a);margin:0 auto 4px}
.partner .name{font-family:"Cormorant Garamond",serif;font-size:9px;color:#fff}
.contact{position:absolute;left:92px;top:456px;right:14px}
.contact h3{font-family:"Montserrat",sans-serif;font-weight:700;font-size:7.5px;letter-spacing:.5px;border-bottom:1px solid var(--gold);padding-bottom:4px;margin-bottom:10px}
.contact li{list-style:none;display:flex;gap:8px;align-items:flex-start;font-family:"Montserrat",sans-serif;font-size:7.4px;line-height:1.3;margin-bottom:8px}
.contact svg{flex:none;width:11px;height:11px}
.contact small{font-size:6.4px;display:block}
/* cover */
.cover .wordmark{position:absolute;top:18px;width:100%;font-size:30px;color:var(--ink)}
.cover .tagline{position:absolute;top:106px;width:100%;color:var(--ink)}
.cover .ring{position:absolute;left:-12px;top:128px;width:274px;height:274px;border-radius:50%;border:6px solid var(--gold);background:#fff;padding:4px}
.cover .ring .photo{width:100%;height:100%;border-radius:50%}
.cover .arc{position:absolute;left:-20px;top:118px}
.sticker{position:absolute;border-radius:50%;background:radial-gradient(circle,#7bbf4a,#3f8a2a)}
.cover .sticker{left:82px;top:350px;width:94px;height:94px}
.headline{position:absolute;top:455px;width:100%;text-align:center;font-family:"Montserrat",sans-serif;font-weight:400;font-size:15.5px;line-height:1.2;color:var(--gold)}
.cover .blurb{position:absolute;top:500px;left:14px;right:14px;text-align:center;font-family:"Montserrat",sans-serif;font-size:8.4px;line-height:1.3;color:var(--text)}
.cover .url{position:absolute;top:560px;width:100%;text-align:center;font-family:"Montserrat",sans-serif;font-size:9.6px;color:var(--gold)}
/* inside left */
.panel--massage .swoosh{position:absolute;left:0;top:0}
.panel--massage .ring{position:absolute;left:52px;top:30px;width:158px;height:158px;border-radius:50%;border:5px solid var(--gold);background:#fff;padding:3px}
.ring .photo{width:100%;height:100%;border-radius:50%}
.panel--massage .list{position:absolute;left:21px;right:21px;top:202px;bottom:18px;display:flex;flex-direction:column}
/* inside right */
.panel--right .brands{position:absolute;top:240px;left:0;width:100%;display:flex;justify-content:center;gap:20px;align-items:center}
.panel--right .sticker{position:static;width:52px;height:52px}
.panel--right .seal-row{display:flex;align-items:center;gap:6px}
.panel--right .seal{width:40px;height:48px;border:2px solid var(--gold);background:linear-gradient(135deg,#a8832a,#e4c977,#a8832a)}
.panel--right .seal-row span{font-family:"Cormorant Garamond",serif;font-size:10px;color:var(--ink)}
.panel--right .wordmark{position:absolute;top:318px;width:100%;font-size:18px;color:var(--ink)}
.panel--right .url{position:absolute;top:350px;width:100%;text-align:center;font-family:"Montserrat",sans-serif;font-size:8.4px;color:var(--text)}
.panel--right .swoosh{position:absolute;right:0;bottom:0}
.panel--right .ring{position:absolute;left:60px;top:420px;width:146px;height:146px;border-radius:50%;border:5px solid var(--gold);background:#fff;padding:3px}
.couples-note{font-size:4.4px!important}
</style>
</head>
<body>

<section class="sheet sheet--outside">
  <!-- Nails -->
  <div class="panel panel--list">
    <h2 class="section-title"><span>HANDS &amp; FEET</span><i></i></h2>
    <p class="lead">Melt into a Pedicure Throne in our Nail Lounge. Our handmade soaks and scrubs are made in house with only the freshest natural and organic ingredients! Your hands and feet have never been loved like this! All nail services include nail and cuticle care, massage and polish of choice.</p>
    <div class="items">
      <div class="item"><div class="item-head"><span class="item-name">Organic Garden Greens Manicure</span><span class="price">$65</span></div><p>Hydrate, smooth and clarify tired and abused hands. Herbal cleansing oil, garden greens exfoliant, and lotus detox hand treatment. <b>55 minutes.</b></p></div>
      <div class="item"><div class="item-head"><span class="item-name">Hot Stone Manicure</span><span class="price">$65</span></div><p>Dissolve tension and stress with the perfect hot stone hand and arm massage. Heal and smooth tired hands with our signature Keratin and Copaiba hot herbal mitts. <b>55 minutes.</b></p></div>
      <div class="item"><div class="item-head"><span class="item-name">Reverse The Hands Of Time Manicure</span><span class="price">$75</span></div><p>The name says it all. Smoothing lava scrub, brightening masque, &amp; luscious tightening hand creme. <b>55 minutes.</b></p></div>
      <div class="item"><div class="item-head"><span class="item-name">Palo Santo Pedicure</span><span class="price">$85</span></div><p>Cleanse and purify to invite only good vibes and great times for 2019 with our handcrafted Palo Santo Pedicure. Palo Santo, "sacred wood" in Spanish (and environmentally friendly, harvested 3 years after it has died naturally), hails from South America as an unparalleled physical and spiritual purifier, &amp; healing anti-inflammatory. Includes our bespoke Bergamot and Balsam foot soak, refreshing Peppermint scrub, and Palo Santo Lotion. <b>55 minutes.</b></p></div>
      <div class="item"><div class="item-head"><span class="item-name">Larkmere Spa Pedicure</span><span class="price">$75</span></div><p>In addition to a classic pedicure, a soothing anti-inflammatory mud mask, paraffin wrap treatment and revitalizing foot, calf massage. Topped off with your choice of enamel. <b>55 minutes.</b></p></div>
      <div class="item"><div class="item-head"><span class="item-name">Mother of Dragonfruit Pedicure</span><span class="price">$85</span></div><p>Breaker of calluses, Reliever of tired feet, Queen of the Catskills, Mother of spring cleaning and perfectly polished toes… Soak. Scrub. Cuticle &amp; Nail Care. Hot stone foot and leg massage. Polish. The Throne. <b>55 minutes.</b></p></div>
      <div class="item"><div class="item-head"><span class="item-name">Grapefruit and Pine Pedicure</span><span class="price">$45</span></div><p>Meet in the middle of sunny spring days and April showers in a pine forest. Refreshing, yet comforting and grounding. A perfect pick me up for any feet that want to celebrate the season! Soak. Scrub. Cuticle &amp; Nail Care. Polish. Boom. <b>30 minutes.</b></p></div>
    </div>
  </div>

  <!-- Back / contact -->
  <div class="panel panel--dark">
    <div class="photo-band" role="img" aria-label="Soft monochrome photo of a guest receiving a facial massage beside rolled towels"></div>
    <div class="wordmark"><span class="w-the">The</span><span class="w-name">Larkmere</span><span class="w-spa">Spa</span></div>
    <div class="tagline">a boutique spa for Men &amp; Women</div>
    <div class="partner"><div class="seal"></div><div class="name">Valoria</div></div>
    <div class="contact">
      <h3>CONTACT US</h3>
      <ul>
        <li><svg viewBox="0 0 12 12"><circle cx="6" cy="6" r="6" fill="#c9a227"/><path d="M3 6.3 6 3.6 9 6.3V9H7V7.2H5V9H3z" fill="#2b2829"/></svg><div>42 Birchwood Hollow Road<br>Larkmere, NY 12590<small>Right off Main Street</small></div></li>
        <li><svg viewBox="0 0 12 12"><circle cx="6" cy="6" r="6" fill="#c9a227"/><path d="M4 3.2h1.3l.6 1.6-.8.6c.4.8 1 1.4 1.8 1.8l.6-.8 1.6.6V8.3C8.8 8.8 8.3 9 7.8 9 5.4 8.7 3.4 6.7 3.1 4.3 3.1 3.7 3.4 3.2 4 3.2z" fill="#2b2829"/></svg><div>(555) 204-3187</div></li>
        <li><svg viewBox="0 0 12 12"><circle cx="6" cy="6" r="6" fill="#c9a227"/><rect x="3" y="4" width="6" height="4.2" fill="#2b2829"/><path d="M3 4l3 2.3L9 4" stroke="#c9a227" stroke-width=".7" fill="none"/></svg><div>info@thelarkmerespa.com</div></li>
        <li><svg viewBox="0 0 12 12"><circle cx="6" cy="6" r="6" fill="#c9a227"/><circle cx="6" cy="6" r="3" fill="none" stroke="#2b2829" stroke-width=".8"/><path d="M3 6h6M6 3c-1.4 1.8-1.4 4.2 0 6M6 3c1.4 1.8 1.4 4.2 0 6" stroke="#2b2829" stroke-width=".6" fill="none"/></svg><div>www.thelarkmerespa.com</div></li>
      </ul>
    </div>
  </div>

  <!-- Front cover -->
  <div class="panel cover">
    <div class="wordmark"><span class="w-the">The</span><span class="w-name">Larkmere</span><span class="w-spa">Spa</span></div>
    <div class="tagline">a boutique spa for Men &amp; Women</div>
    <svg class="arc" width="300" height="300" viewBox="0 0 300 300"><path d="M200 14 A140 140 0 0 1 290 150" stroke="#231f20" stroke-width="2" fill="none"/></svg>
    <div class="ring"><div class="photo" role="img" aria-label="Photo of a woman relaxing face down during a back massage, a flower tucked behind her ear"></div></div>
    <div class="sticker" role="img" aria-label="Clear Spa certification sticker"></div>
    <h1 class="headline">ESCAPE THE CONGESTION<br>OF EVERYDAY LIFE</h1>
    <p class="blurb">Located in the heart of the Catskill Mountains, our down-to-earth staff, laid back atmosphere, and extraordinary services leave no room for pretenses.</p>
    <div class="url">www.thelarkmerespa.com</div>
  </div>
</section>

<section class="sheet sheet--inside">
  <!-- Massages -->
  <div class="panel panel--massage">
    <svg class="swoosh" width="252" height="210" viewBox="0 0 252 210"><path d="M0 0H232C220 60 170 100 110 130 60 155 20 170 0 200Z" fill="#231f20"/><path d="M232 0C220 60 170 100 110 130 60 155 20 172 0 205" stroke="#c9a227" stroke-width="4" fill="none"/></svg>
    <div class="ring"><div class="photo" role="img" aria-label="Photo of a woman with closed eyes receiving a shoulder massage"></div></div>
    <div class="list">
      <h2 class="section-title"><span>MASSAGES</span><i></i></h2>
      <p class="lead">Tired, sore muscles, and exhausted minds are refreshed by the perfect massage customized to your individual needs.</p>
      <div class="items">
        <div class="item"><div class="item-head"><span class="item-name">Hot Stone</span><span class="price">$175</span></div><p>Unforgettable. Warm basalt lava stones melt away all stress and tension in sore muscles &amp; joints. The ultimate Aprés ski treat. <b>90 minutes.</b></p></div>
        <div class="item"><div class="item-head"><span class="item-name">Pulsar Rapid Recovery Massage</span><span class="price">$135</span></div><p>Recover faster and feel better while optimizing your massage time with our Pulsar compression massage. Dynamic air compression mobilizes fluid, speeds recovery time and massages tired and aching muscles for fresh legs on the go! Includes head, neck, shoulders, arm and hand massage. <b>55 minutes.</b></p></div>
        <div class="item"><div class="item-head"><span class="item-name">Swedish Massage</span><span class="price">$105/$160</span></div><p>Relaxing and therapeutic. Ease tension and enhance circulation. Great for a first time massage or any spa veteran. <b>55 or 90 minutes.</b></p></div>
        <div class="item"><div class="item-head"><span class="item-name">Deep Tissue</span><span class="price">$115/$175</span></div><p>A therapeutic combination of slow and deep pressure alleviates chronic pain, muscle fatigue, and limited range of motion. Muscle Therapy lotion or creme. <b>55 or 90 minutes.</b></p></div>
        <div class="item"><div class="item-head"><span class="item-name">Tension Tamer</span><span class="price">$125/$195</span></div><p>Head, neck and shoulders. Deep Tissue with hot towels, muscle soothing oils, and cupping. <b>55 or 90 minutes.</b></p></div>
        <div class="item"><div class="item-head"><span class="item-name">Recovery</span><span class="price">$110/$170</span></div><p>Specific to your athletic needs, whether pro or a weekend warrior. Relax, stretch and recover. <b>55 or 90 minutes.</b></p></div>
      </div>
    </div>
  </div>

  <!-- Facials middle -->
  <div class="panel panel--list">
    <div class="item"><div class="item-head"><span class="item-name">Prenatal</span><span class="price">$115</span></div><p>Ultimate treat for Mother-to-be. Soothes aches &amp; pains during pregnancy. Mother must be out of first trimester. <b>55 minutes.</b></p></div>
    <div class="item" style="margin-top:10px"><div class="item-head"><span class="item-name">Couples</span><span class="price">$210 &amp;up</span></div><p class="couples-note">For lovebirds or loved ones. Relax and recoup with your favorite person. 55 or 90 minutes.</p></div>
    <h2 class="section-title" style="margin-top:46px"><span>FACIALS</span><i></i></h2>
    <p class="lead">Featuring Valoria Skincare products our organic and botanical facials are perfect for even the most sensitive skin! Whether you want to erase fine lines and wrinkles, treat problem skin, or just relax, an unforgettable experience awaits you. All 55+ minute facial treatments include a glorious head, neck, shoulder, arm and hand massage.</p>
    <div class="items">
      <div class="item"><div class="item-head"><span class="item-name">Detox Facial</span><span class="price">$135</span></div><p>Organically remove damage, congestion and imperfections. Ideal for blemishes that won't heal, acne, &amp; fine lines. Increases oxygen &amp; blood flow to dramatically reboot your skins natural healing abilities and reveal healthier skin. <b>55 minutes.</b></p></div>
      <div class="item"><div class="item-head"><span class="item-name">B.L.T. Facial</span><span class="price">$145</span></div><p>Brighten. Lighten. Tighten - Organic triple peel, also known as our "Runway Peel" because it leaves you glowing and ready for the red carpet immediately, leaves you fresh and glowing, boosts collagen, and is hydrating. Ideal for treating hyper-pigmentation. <b>55 minutes.</b></p></div>
      <div class="item"><div class="item-head"><span class="item-name">Double Down Facial</span><span class="price">$165</span></div><p>Who says you can't multi task and relax?! Detox, tighten and increase circulation with our all time favorite peel, followed by our top of the line multi-acid peel. Resurface, smooth, brighten and hydrate. This power hour facial is a one stop shop for all your skincare needs. Extractions and custom masque always included. Head, neck, shoulders, arm and hand massage obligatory. <b>55 minutes.</b></p></div>
      <div class="item"><div class="item-head"><span class="item-name">Organic Masque Montage</span><span class="price">$115</span></div><p>Three layers of customized masques created exclusively for your skin type. Includes steam, cleanse, exfoliation, extractions, masques, massage, and moisturizer. <b>55 minutes.</b></p></div>
      <div class="item"><div class="item-head"><span class="item-name">Soothing Skin Facial</span><span class="price">$125</span></div><p>Rosacea and sensitive skin be damned! This facial was made for you, you sensitive souls! Combat redness, irritation and dryness. Gentle, yet effective for even the most sensitive skin types. Soothe, hydrate, and refresh. <b>$125 - 55 mins</b><br><b>+ Botanical AHA (Alpha Hydroxy Acid)</b> Peel add-on formulated especially for sensitive and rosacea skin types. <b>$50</b></p></div>
    </div>
  </div>

  <!-- Facials right -->
  <div class="panel panel--right">
    <div style="position:absolute;left:21px;right:21px;top:18px">
      <div class="item"><div class="item-head"><span class="item-name">Island Fruit Facial</span><span class="price">$135</span></div><p>Minimize pore size and surface build up with zero down time. Our organic lactic acid peel leaves skin smooth, clarified and glowing! Custom masque included. Ideal for all skin types. <b>55 minutes.</b></p></div>
      <div class="item" style="margin-top:12px"><div class="item-head"><span class="item-name">Microdermabrasion</span><span class="price">$115</span></div><p>Reduce wrinkles, scarring, discoloration, sun damage, large pores and age spots. Stimulate collagen and elastin production through diamond and crystal exfoliation. Best in series of six. <b>30min. Add To Facial +$65</b></p></div>
      <div class="item" style="margin-top:12px"><div class="item-head"><span class="item-name">R&amp;R Facial</span><span class="price">$255 (Reg. $275)</span></div><p>Radiance &amp; Revenge. Let's cut to the chase- Our most dynamic results oriented facial, and the ultimate kick start to rebooting skin after a long summer of sunshine and heat… or making sure you are smoking hot and 10 years younger when you see your ex. Microdermabrasion. Double Peel facial. LED. (Light Emitting Diode) Boom. (as in WOW!) <b>90 minutes.</b></p></div>
    </div>
    <div class="brands">
      <div class="sticker" role="img" aria-label="Clear Spa certification sticker"></div>
      <div class="seal-row"><div class="seal"></div><span>Valoria</span></div>
    </div>
    <div class="wordmark">The Larkmere Spa</div>
    <div class="url">www.thelarkmerespa.com</div>
    <svg class="swoosh" width="252" height="250" viewBox="0 0 252 250"><path d="M252 0V250H20C40 190 90 130 150 90 195 60 230 30 252 0Z" fill="#231f20"/><path d="M252 0C230 30 195 60 150 90 90 130 40 190 20 250" stroke="#c9a227" stroke-width="4" fill="none"/></svg>
    <div class="ring"><div class="photo" role="img" aria-label="Photo of a woman in a white head towel having a facial masque brushed on"></div></div>
  </div>
</section>

</body>
</html>
```